Halvorn Hire Business Card Design

Need business cards designed for our new equipment rental. We specialize in renting to landscape / tree professionals, contractors, Do-It-Yourself'ers and Around the home or office. Looking for a eye catching card. Landscape and construction should be the theme. The logo is attached, and you can see our colors from the logo. You can use whatever color goes with it ok.

Target Market(s)

First off Landscape and Tree Professional. Then contractors, Do-It-Yourself'ers and rentals for Around the home or office.

Industry/Entity Type

Business

Contact Information for Business Card

Eye catching background that blends landscaping with construction equipment

Requirements
Must have
• Name on Card will Be: Derek Pollard (Manager)
• My Direct Phone Number is: 352-418-7093
• derek@halvornhire.example
• www.halvornhire.example
• 4172 Wexley Mill Road,
• Dade City FL 33590
Nice to have
• Would be Nice to have these bullets on the Face of the card that does not have all my information.
• Serving:
• Landscape / Tree Professionals
• Contractors
• DYI'ers or say Do-It-Yourself'ers
• Maybe have serving small and centered above these bullets, and these 3 bullets along the bottom of the card. Ideas?

```html
<!DOCTYPE html>
<html lang="en">
<head>
<meta charset="utf-8">
<title>Halvorn Hire – Business Cards</title>
<link href="https://fonts.googleapis.com/css2?family=Lato:wght@400;700;900&display=swap" rel="stylesheet">
<style>
  :root{
    --navy:#0f426d;
    --gold:#f9bf6b;
    --grey:#9a9a9a;
    --paper:#ffffff;
    --backdrop:#2a2a2c;
  }
  *{margin:0;padding:0;box-sizing:border-box}
  html,body{width:1200px;height:880px;overflow:hidden;background:var(--backdrop)}
  body{position:relative;font-family:'Lato',sans-serif}
  .card{
    position:absolute;left:260px;width:680px;height:388px;
    background:var(--paper);border-radius:22px;overflow:hidden;
    box-shadow:0 10px 30px rgba(0,0,0,.45);
  }
  .card--front{top:35px}
  .card--back{top:458px}

  .brand{display:flex;align-items:center;gap:12px}
  .brand__mark{width:22px;height:22px;background:var(--grey);flex:none}
  .brand__name{font-weight:900;color:var(--navy);font-size:46px;letter-spacing:1px;white-space:nowrap}

  .card--front .brand{position:absolute;left:0;right:0;top:120px;justify-content:center}
  .services{position:absolute;left:0;right:0;top:228px;text-align:center;color:var(--navy);font-size:19px;line-height:1.45}
  .services__dot{display:inline-block;width:9px;height:9px;border-radius:50%;background:var(--gold);margin:0 8px 2px 14px;vertical-align:middle}

  .card--back .brand{position:absolute;left:40px;top:125px}
  .card--back .brand__mark{width:20px;height:20px}
  .card--back .brand__name{font-size:36px}
  .wave{position:absolute;inset:0;width:680px;height:388px}
  .person{position:absolute;right:40px;top:36px;text-align:right}
  .person__name{font-weight:900;color:var(--navy);font-size:24px}
  .person__role{color:var(--gold);font-size:17px;margin-top:2px}
  .contact{position:absolute;right:36px;top:212px;text-align:right;color:#fff;font-size:15px;line-height:1.5}
  .contact__row{display:flex;justify-content:flex-end;align-items:center;gap:8px}
  .contact__icon{width:18px;height:18px;border:1.5px solid var(--gold);border-radius:50%;display:flex;align-items:center;justify-content:center;flex:none}
  .contact__spacer{width:18px;flex:none}
</style>
</head>
<body>

<section class="card card--front" aria-label="Card front">
  <div class="brand">
    <span class="brand__mark"></span>
    <span class="brand__name">HALVORN HIRE</span>
  </div>
  <p class="services">
    <span class="services__dot"></span>Landscape / Tree Professionals<span class="services__dot"></span>Contractors<br>
    <span class="services__dot"></span>DYI'ers or say Do-It-Yourself'ers
  </p>
</section>

<section class="card card--back" aria-label="Card back">
  <svg class="wave" viewBox="0 0 680 388" aria-hidden="true">
    <path d="M0 305 C170 312 290 290 330 200 C315 290 220 328 0 332 Z" fill="var(--gold)"/>
    <path d="M610 92 C500 110 430 165 378 245 C325 322 240 340 150 346" fill="none" stroke="var(--navy)" stroke-width="7" stroke-linecap="round"/>
    <path d="M680 95 C540 100 460 150 400 240 C340 330 220 350 0 352 L0 388 L680 388 Z" fill="var(--navy)"/>
  </svg>

  <div class="brand">
    <span class="brand__mark"></span>
    <span class="brand__name">HALVORN HIRE</span>
  </div>

  <div class="person">
    <div class="person__name">Derek Pollard</div>
    <div class="person__role">Manager</div>
  </div>

  <div class="contact">
    <div class="contact__row">4172 Wexley Mill Road,<span class="contact__spacer"></span></div>
    <div class="contact__row">Dade City FL 33590<span class="contact__spacer"></span></div>
    <div class="contact__row">352-418-7093
      <span class="contact__icon"><svg width="10" height="10" viewBox="0 0 10 10"><rect x="2.5" y="0.5" width="5" height="9" rx="1" fill="none" stroke="var(--gold)"/></svg></span></div>
    <div class="contact__row">derek@halvornhire.example
      <span class="contact__icon"><svg width="10" height="10" viewBox="0 0 10 10"><rect x="0.5" y="2" width="9" height="6" fill="none" stroke="var(--gold)"/><path d="M0.5 2 L5 5.5 L9.5 2" fill="none" stroke="var(--gold)"/></svg></span></div>
    <div class="contact__row">www.halvornhire.example
      <span class="contact__icon"><svg width="10" height="10" viewBox="0 0 10 10"><circle cx="5" cy="5" r="4.3" fill="none" stroke="var(--gold)"/><path d="M0.7 5 H9.3 M5 0.7 C2.5 3 2.5 7 5 9.3 M5 0.7 C7.5 3 7.5 7 5 9.3" fill="none" stroke="var(--gold)"/></svg></span></div>
  </div>
</section>

</body>
</html>
```